依頼概要
<概要>
ものづくり(製造業)展示会に出展するにあたり、展示用のポスターのデザインを作成していただきたい。

<詳細>
・本展示会は国内最大の展示会(精密部材総合フェア 通称:P-Fair)です。
・来場者は数万人で出展企業も数百社ある。
・出展スペースは3m x 3mです。
・弊社のコーポレートカラーはブルーです。
(ウェブサイトを参照、または添付ロゴデータをご確認ください)
・ポスターサイズはA1縦で枚数は4パターン(まったく内容が異なるもの)
・薄利多売を目的とした出展PRではない。
・ポスターを掲示する壁の色は白です。

<強み/ポイント>
・創業53年目の老舗会社
・社員の平均年齢29.8歳(従業員数:25名 役員とベトナムの社員4名を含む)
・ベトナム(ホーチミン市)に設計事務所を構えている
・設計力がある(できる)
・最新鋭の工作機械(設備)を有している
・比較的高収益企業

<事業領域>
・自動車
・医療
・航空/宇宙
・エネルギー

<弊社の概要>
弊社は治具や工具などお客様が求める生産に必要な設備(道具)をお客様の仕様や要望に沿って、設計・製作・組立をしている会社です。設計では3DCADを使用し、できた設計データをお客様に承認していただき、最新鋭の工作機械(マシニングセンター、NC旋盤)を使用して金属の様々な材料(アルミ・鉄・樹脂)などを加工し、最後にそれぞれの部品を組立ます。通常、製造業者の多くはお客様から図面がきてその図面通りの部品を必要数加工をして納入するという部品加工業タイプが多いですが、弊社は自社で設計から行っているのでものを生み出す(アイデアを出す)という技術力を持っており、かつそのほとんどが一品一様です。
また、ベトナムのホーチミン市で現地スタッフ4名を雇用し、機械や金型、治具などというものの設計をしています。(日本も同様です。ただし、日本は製造もあります)ベトナム人は日本語が堪能で、うち2名は本社勤務経験あり。

<ポスターに求めるもの>
・シンプルで目に入ってきやすくインパクトが欲しい。(文字が多いのはNGです)
・3パターンとも色の統一感は必要です。
・製造業ですが、デザイン性を求めています。

<ポスターの内容>
1枚目/2枚目
ベトナムの国旗を大きく必ず入れてほしく、ベトナムの地図なども。言葉ととしては、例:ベトナムのチカラ、Engineered by Vietnames、ベトナムあります!など。。。つまり、ベトナムでの設計を請負える、またはベトナム事業を提案する。というようなイメージにつながりやすいポスターにしたいです。1枚目と2枚目は異なった視点から捉える内容にしていただきたいです。

3枚目
設計・加工・組立までの一貫したプロセスのサービス力の高さがPRできるような、またはそのような印象を受けるようなポスターにしたいです。

4枚目
上記情報を基にデザイナーに一任します。

以上、よろしくお願い致します。ご不明な点がありましたら、お気軽にお問い合わせください。
また、画像などが必要な際はウェブサイトやパンフレットを作成した際のデータがあるので、お問い合わせください。
URL:http;//www.kisemura.co.jp/
■ 選んだ理由

ビジュアルアイコンで分かりやすくしていただいた点。

■ 提案者全員のお礼・コメント

ご提案をいただいた皆さま、限られた時間の中でありがとうございました。
採用させていただいたデザイン以外にも甲乙つけ難いものばかりで想定以上に選定に迷いました。
また、機会がありましたらよろしくお願いいたします。

```html
<!DOCTYPE html>
<html lang="en">
<head>
<meta charset="utf-8">
<title>Let's meet in Vietnam next time — KISEMURA</title>
<link rel="stylesheet" href="https://fonts.googleapis.com/css2?family=Archivo+Black&family=Noto+Sans+JP:wght@700&family=Roboto:wght@500;700&display=swap">
<style>
  :root {
    --paper: #f8f4e6;
    --flag-red: #e0201b;
    --flag-yellow: #ffe100;
    --ink: #111111;
    --land-green: #86c440;
    --city-red: #d8261e;
    --brand-navy: #1d3f7a;
    --white: #ffffff;
  }
  * { margin: 0; padding: 0; box-sizing: border-box; }
  html, body { width: 849px; height: 1200px; overflow: hidden; background: var(--paper); }
  .poster { position: relative; width: 849px; height: 1200px; background: var(--paper); overflow: hidden; }

  .event-tag {
    position: absolute; top: 0; right: 0; height: 26px; padding: 0 14px;
    background: var(--brand-navy); color: var(--white);
    display: flex; align-items: center; gap: 6px;
    font-family: "Noto Sans JP", sans-serif; font-weight: 700; font-size: 14px; letter-spacing: 0.5px;
  }
  .event-tag .edition { font-size: 9px; }

  .flag { position: absolute; left: 51px; top: 51px; width: 747px; height: 594px; }

  .headline {
    position: absolute; left: 0; top: 472px; width: 849px; text-align: center;
    font-family: "Archivo Black", "Arial Black", sans-serif; color: var(--ink);
    font-size: 96px; line-height: 80px; letter-spacing: -3px;
  }
  .headline span { display: block; }

  .map-area {
    position: absolute; left: 340px; top: 815px; width: 130px; height: 290px;
    background: var(--land-green); border-radius: 40px 30px 50px 20px;
  }
  .city {
    position: absolute; display: flex; align-items: center; gap: 5px;
    font-family: "Roboto", sans-serif; font-weight: 700; font-size: 11px; color: var(--ink);
  }
  .city::before { content: ""; width: 9px; height: 9px; border-radius: 50%; background: var(--city-red); }
  .city-hanoi { left: 400px; top: 838px; }
  .city-hcm { left: 376px; top: 1070px; }

  .brand {
    position: absolute; right: 40px; bottom: 30px;
    display: flex; align-items: center; gap: 10px; color: var(--brand-navy);
  }
  .brand-dot { width: 40px; height: 40px; border-radius: 50%; background: var(--brand-navy); }
  .brand-name { font-family: "Roboto", sans-serif; font-weight: 700; font-size: 28px; letter-spacing: 2px; line-height: 1; }
  .brand-sub { font-family: "Roboto", sans-serif; font-weight: 700; font-size: 8px; letter-spacing: 1px; margin-top: 3px; }
</style>
</head>
<body>
<main class="poster">
  <div class="event-tag"><span class="edition">第10回</span><span>精密部材総合フェア</span></div>

  <svg class="flag" viewBox="51 51 747 594" role="img" aria-label="Flag of Vietnam">
    <rect x="51" y="51" width="747" height="594" fill="var(--flag-red)"/>
    <polygon fill="var(--flag-yellow)" points="425,143 456.5,239.7 558.1,239.7 475.9,299.5 507.3,396.3 425,336.5 342.7,396.3 374.1,299.5 291.9,239.7 393.5,239.7"/>
  </svg>

  <h1 class="headline">
    <span>Let's meet</span>
    <span>in</span>
    <span>Vietnam</span>
    <span>next time</span>
  </h1>

  <div class="map-area" role="img" aria-label="Green map of Vietnam marking Ha Noi and Ho Chi Minh City"></div>
  <div class="city city-hanoi">Ha Noi</div>
  <div class="city city-hcm">Ho Chi Minh</div>

  <div class="brand">
    <div class="brand-dot"></div>
    <div>
      <div class="brand-name">KISEMURA</div>
      <div class="brand-sub">DESIGN &amp; MANUFACTURING COMPANY</div>
    </div>
  </div>
</main>
</body>
</html>
```